Coral Beacon Stationery Design Project

I am looking for a suitable stationary design for my company Coral Beacon Pty Ltd (ACN 582 914 306).

The requirements can be better explained by visiting my website
"coral-beacon-trust.org"

I will be sending letters to Ministers of State and the Heads of Government Agencies so the theme needs to be formal and serious.

A theme with a shield or similar picking on the "guardian" concept would be appropriate

Target Market(s)

Ministers of State and Department Agency Heads and legal firms, the heads of Trustee Companies as well as Members of Coral Beacon

Industry/Entity Type

Government

Requirements
Must have
• Letterhead design is a priority - Business Card secondary

Must include tag line "Steady hands for every estate we tend" with a registered trade mark superscript at the end that is an R in a circle {Windows Alt +0174 on numeric keypad or Mac Option +R}.

Must include website address "Coral-Beacon-Trust.org" plus Email address "corbeacon@mailvessel.net

Company name "Coral Beacon Pty. Ltd." and Australian Company Number "ACN 582 914 306" needs to be shown more discretely

Address is "47 Finch Crescent, Marrowdale, 3291"
Nice to have
• A watermark is something to be considered

```html
<!DOCTYPE html>
<html lang="en">
<head>
<meta charset="utf-8">
<title>Coral Beacon Pty Ltd — Business Cards</title>
<link href="https://fonts.googleapis.com/css2?family=Arimo:wght@400;700&display=swap" rel="stylesheet">
<style>
  :root {
    --backdrop: #e4e4e6;
    --purple: #74248a;
    --purple-deep: #4a1159;
    --purple-text: #6f2384;
    --ink: #2b2b2b;
    --paper: #ffffff;
    --watermark: #ece8f0;
  }
  * { box-sizing: border-box; margin: 0; padding: 0; }
  html, body { width: 1200px; height: 880px; overflow: hidden; }
  body {
    background: var(--backdrop);
    font-family: "Arimo", Arial, sans-serif;
    position: relative;
  }
  .card {
    position: absolute;
    width: 600px;
    height: 343px;
    overflow: hidden;
    box-shadow: 0 6px 18px rgba(0,0,0,0.18);
  }

  /* Front */
  .card-front {
    left: 300px;
    top: 60px;
    background: linear-gradient(115deg, var(--purple) 0%, #661c7b 55%, var(--purple-deep) 100%);
  }
  .front-brand {
    position: absolute;
    left: 70px;
    top: 92px;
    display: flex;
    align-items: center;
    gap: 20px;
  }
  .brand-dot {
    width: 64px; height: 64px;
    border-radius: 50%;
    background: var(--paper);
    opacity: 0.9;
    flex: none;
  }
  .front-name {
    color: var(--paper);
    font-weight: 700;
    font-size: 38px;
    line-height: 1.02;
  }
  .front-tagline {
    position: absolute;
    left: 70px;
    top: 178px;
    color: var(--paper);
    font-size: 17px;
    letter-spacing: 0.3px;
  }
  .front-tagline sup { font-size: 10px; }
  .front-footer {
    position: absolute;
    left: 0; right: 0; bottom: 0;
    height: 58px;
    background: var(--paper);
    clip-path: polygon(0 30%, 100% 0, 100% 100%, 0 100%);
    display: flex;
    align-items: flex-end;
    padding: 0 0 14px 90px;
  }
  .front-url {
    color: var(--purple-text);
    font-size: 15px;
    letter-spacing: 0.5px;
  }

  /* Back */
  .card-back {
    left: 300px;
    top: 463px;
    background: var(--paper);
  }
  .back-swoosh { position: absolute; left: 0; top: 0; }
  .back-watermark {
    position: absolute;
    right: 40px;
    bottom: 30px;
    width: 200px; height: 200px;
    border-radius: 50%;
    background: var(--watermark);
  }
  .back-brand {
    position: absolute;
    left: 34px;
    top: 26px;
    display: flex;
    align-items: center;
    gap: 10px;
  }
  .back-brand .brand-dot {
    width: 30px; height: 30px;
    background: var(--purple);
    opacity: 1;
  }
  .back-name {
    color: var(--purple-text);
    font-weight: 700;
    font-size: 18px;
    line-height: 1.05;
  }
  .back-tagline {
    position: absolute;
    left: 74px;
    top: 68px;
    font-size: 9px;
    color: var(--ink);
  }
  .back-tagline sup { font-size: 6px; }
  .contact {
    position: absolute;
    left: 34px;
    top: 100px;
    font-size: 14px;
    color: var(--ink);
    line-height: 1.35;
  }
  .person-name { color: var(--purple-text); font-weight: 700; font-size: 18px; }
  .person-role { margin-bottom: 12px; }
  .company { color: var(--purple-text); font-weight: 700; }
  .label { color: var(--purple-text); }
</style>
</head>
<body>

  <section class="card card-front" aria-label="Business card front">
    <div class="front-brand">
      <span class="brand-dot"></span>
      <div class="front-name">Coral Beacon<br>Pty Ltd</div>
    </div>
    <p class="front-tagline">Steady hands for every estate we tend<sup>®</sup></p>
    <div class="front-footer">
      <span class="front-url">www.Coral-Beacon-Trust.org</span>
    </div>
  </section>

  <section class="card card-back" aria-label="Business card back">
    <svg class="back-swoosh" width="600" height="343" viewBox="0 0 600 343" aria-hidden="true">
      <path d="M0 300 C 150 312, 330 330, 600 343 L 0 343 Z" fill="var(--purple)"/>
    </svg>
    <div class="back-watermark"></div>

    <div class="back-brand">
      <span class="brand-dot"></span>
      <div class="back-name">Coral Beacon<br>Pty Ltd</div>
    </div>
    <p class="back-tagline">Steady hands for every estate we tend<sup>®</sup></p>

    <div class="contact">
      <div class="person-name">ALEX MORROW</div>
      <div class="person-role">Position</div>
      <div class="company">Coral Beacon Pty Ltd</div>
      <div>47 Finch Crescent, Marrowdale, 3291</div>
      <div><span class="label">p:</span> 555.218.4409</div>
      <div><span class="label">e:</span> corbeacon@mailvessel.net</div>
      <div><span class="label">w:</span> www.Coral-Beacon-Trust.org</div>
    </div>
  </section>

</body>
</html>
```